Hi,
We are also sourcing for a logo, if you have ideas please take a look at our other project (if you look at our profile you should be able to see it).
We are looking for a website that will be used to manage mobile devices. The feature set is rather small, users can Wipe, Lock, Locate devices as well as make them Ring or Speak (by sending text to be spoken). We attached some images of what it looks like right now. We are looking for simplicity, uniformity and most importantly, the website should be thought of as primary User Interface, it should flow.
Please see attached to get an idea of what it looks like now. The current design was inspired by making a site that will work and flow well on a variety of displays (from mobile to tablet to desktop).
We want to stay away from radio buttons, check-boxes. This should be engaging and creative, opposite of Corporate. Not busy (ideally we are looking to have fewest possible choices at any given time and at the same time no feature should be more than 3 clicks away (this is a suggestion/approximation... just want to share our understanding of what 'flow' is).
Could be cartoony.
Thanks!
BrisketLoom
Reason: there are a couple of designs that are interesting, in addition to specific feedback I provided, possibly looking for more concepts.
Thank You

```html
<!DOCTYPE html>
<html lang="en">
<head>
<meta charset="utf-8">
<title>BrisketLoom</title>
<link rel="stylesheet" href="https://fonts.googleapis.com/css2?family=Archivo+Black&family=Arimo:wght@400;700&display=swap">
<style>
  :root {
    --page-bg: #ffffff;
    --ink: #111111;
    --muted-ink: #666666;
    --text-blue: #0a0ae6;
    --text-blue-soft: #a0a0f2;
    --find-green: #2b6008;
    --find-green-soft: #94a878;
    --secure-red: #f20a0a;
    --secure-red-soft: #f6a4a4;
    --badge-black: #000000;
    --badge-edge: #a6a6a6;
    --panel-border: #c4c4c4;
    --field-border: #c9c9c9;
    --button-top: #f6f6f6;
    --button-bottom: #dedede;
    --link-blue: #2a7ad2;
    --skyline: #111111;
  }
  * { box-sizing: border-box; margin: 0; padding: 0; }
  html, body { width: 1200px; height: 675px; overflow: hidden; background: var(--page-bg); }
  body { font-family: "Arimo", Arial, sans-serif; color: var(--ink); }
  .canvas { position: relative; width: 1200px; height: 675px; overflow: hidden; }

  .intro {
    position: absolute; left: 169px; top: 106px; width: 490px;
    font-size: 17px; line-height: 20.5px;
  }
  .intro em { font-weight: 700; font-style: italic; }

  .store-badge {
    position: absolute; left: 718px; top: 110px; width: 156px; height: 53px;
    background: var(--badge-black); border: 1px solid var(--badge-edge); border-radius: 7px;
  }

  .feature { position: absolute; left: 169px; width: 460px; height: 122px; }
  .feature svg { position: absolute; left: 0; top: 0; }
  .feature-copy { position: absolute; font-size: 17px; line-height: 20.5px; }
  .feature-title {
    font-family: "Archivo Black", "Arial Black", sans-serif;
    font-size: 21px; font-weight: 400; line-height: 24px; letter-spacing: 0.6px;
  }
  .feature--text { top: 204px; }
  .feature--text .feature-copy { left: 146px; top: 22px; }
  .feature--find { top: 332px; }
  .feature--find .feature-copy { left: 151px; top: 16px; }
  .feature--secure { top: 460px; }
  .feature--secure .feature-copy { left: 151px; top: 14px; }

  .login-panel {
    position: absolute; left: 722px; top: 290px; width: 302px; height: 177px;
    border: 1px solid var(--panel-border); border-radius: 3px; background: var(--page-bg);
  }
  .login-field {
    position: absolute; left: 18px; width: 251px; height: 27px;
    border: 1px solid var(--field-border); border-radius: 3px;
    font-family: inherit; font-size: 12px; color: var(--muted-ink); padding: 0 7px; background: #fff;
  }
  .login-field::placeholder { color: #7a7a7a; }
  .login-field--email { top: 23px; }
  .login-field--password { top: 70px; }
  .login-button {
    position: absolute; left: 20px; top: 120px; width: 66px; height: 36px;
    border: 1px solid #b8b8b8; border-radius: 3px;
    background: linear-gradient(var(--button-top), var(--button-bottom));
    font-family: inherit; font-size: 15px; color: #333;
  }
  .forgot-link {
    position: absolute; left: 129px; top: 140px;
    font-size: 12px; color: var(--link-blue); text-decoration: none;
  }

  .skyline {
    position: absolute; left: 0; bottom: 0; width: 1200px; height: 80px;
    background: linear-gradient(to bottom, rgba(17,17,17,0) 0%, rgba(17,17,17,0.85) 25%, var(--skyline) 50%);
  }
</style>
</head>
<body>
<main class="canvas">
  <p class="intro">BrisketLoom is a cloud based service that allows individuals, parents and businesses to manage and control mobile devices remotely. <em>Contact</em> us for a free consultation.</p>

  <div class="store-badge" role="img" aria-label="App store download badge"></div>

  <section class="feature feature--text">
    <svg width="108" height="122" viewBox="0 0 108 122" aria-hidden="true">
      <polyline points="54,1 1,30 1,92 54,121" fill="none" stroke="var(--text-blue-soft)" stroke-width="2"/>
      <polygon points="54,0 108,30 108,92 54,122" fill="var(--text-blue)"/>
      <path d="M66 42 h26 a5 5 0 0 1 5 5 v22 a5 5 0 0 1 -5 5 h-14 l-12 10 l3 -10 h-3 z" fill="#fff"/>
    </svg>
    <div class="feature-copy">
      <h2 class="feature-title">text</h2>
      <p>use a computer, tablet or a phone<br>to send and get text messages</p>
    </div>
  </section>

  <section class="feature feature--find">
    <svg width="108" height="122" viewBox="0 0 108 122" aria-hidden="true">
      <polyline points="54,1 1,30 1,92 54,121" fill="none" stroke="var(--find-green-soft)" stroke-width="2"/>
      <polygon points="54,0 108,30 108,92 54,122" fill="var(--find-green)"/>
      <circle cx="77" cy="56" r="13" fill="none" stroke="#fff" stroke-width="5"/>
      <line x1="86" y1="66" x2="98" y2="79" stroke="#fff" stroke-width="6" stroke-linecap="round"/>
    </svg>
    <div class="feature-copy">
      <h2 class="feature-title">find</h2>
      <p>on a map<br>make it ring<br>make it speak</p>
    </div>
  </section>

  <section class="feature feature--secure">
    <svg width="108" height="122" viewBox="0 0 108 122" aria-hidden="true">
      <polyline points="54,1 1,30 1,92 54,121" fill="none" stroke="var(--secure-red-soft)" stroke-width="2"/>
      <polygon points="54,0 108,30 108,92 54,122" fill="var(--secure-red)"/>
      <path d="M71 56 v-9 a11 11 0 0 1 22 0 v9" fill="none" stroke="#fff" stroke-width="5"/>
      <rect x="64" y="55" width="36" height="32" rx="3" fill="#fff"/>
      <circle cx="82" cy="67" r="4" fill="var(--secure-red)"/>
      <rect x="80" y="68" width="4" height="10" fill="var(--secure-red)"/>
    </svg>
    <div class="feature-copy">
      <h2 class="feature-title">secure</h2>
      <p>set a password<br>lock it<br>wipe it clean</p>
    </div>
  </section>

  <form class="login-panel">
    <input class="login-field login-field--email" type="text" placeholder="Email" aria-label="Email">
    <input class="login-field login-field--password" type="password" placeholder="Password" aria-label="Password">
    <button class="login-button" type="button">Login</button>
    <a class="forgot-link" href="#">forgot your password?</a>
  </form>

  <div class="skyline" role="img" aria-label="City skyline silhouette along the bottom edge"></div>
</main>
</body>
</html>
```